Logo for Internal Medicine practice

I want a logo for my Internal Medicine practice, I would like it to be with my name on it which is Lucía Barrenechea Ruiz.

I would like the business card to say the following (it is in Spanish since my practice is in Spanish):

Lucía Barrenechea Ruiz
Medicina Interna
Cel. 5583617204
luciabarrenechearuiz@correovela.mx

Logo Text

Lucía Barrenechea

```html
<!DOCTYPE html>
<html lang="es">
<head>
<meta charset="utf-8">
<title>Lucía Barrenechea — Medicina Interna</title>
<link rel="stylesheet" href="https://fonts.googleapis.com/css2?family=Cinzel:wght@400;700&family=Questrial&display=swap">
<style>
  :root {
    --teal: #0a8890;
    --teal-light: #45a3a6;
    --paper: #efefef;
    --grey-light: #ffffff;
    --grey-dark: #c6c6c6;
    --ink: #4a4a4a;
    --white: #ffffff;
  }
  * { margin: 0; padding: 0; box-sizing: border-box; }
  html, body { width: 1200px; height: 1200px; overflow: hidden; }
  body {
    position: relative;
    background: var(--paper);
    font-family: "Questrial", sans-serif;
  }
  .brand-mark {
    position: absolute;
    left: 0; top: 0;
    width: 1200px; height: 856px;
    display: flex;
    align-items: center;
    justify-content: center;
  }
  .brand-name {
    font-family: "Cinzel", serif;
    font-weight: 400;
    color: var(--teal);
    font-size: 74px;
    letter-spacing: 2px;
    white-space: nowrap;
  }
  .card {
    position: absolute;
    top: 856px;
    width: 600px;
    height: 344px;
  }
  .card--front {
    left: 0;
    background: radial-gradient(ellipse 60% 65% at 50% 35%, var(--teal-light) 0%, var(--teal) 100%);
    display: flex;
    align-items: center;
    justify-content: center;
  }
  .card--front .brand-name {
    color: var(--white);
    font-size: 32px;
    letter-spacing: 1px;
  }
  .card--back {
    left: 600px;
    background: radial-gradient(ellipse 45% 55% at 50% 50%, var(--grey-light) 0%, var(--grey-dark) 100%);
  }
  .card--back .brand-name {
    position: absolute;
    right: 30px;
    top: 62px;
    font-size: 20px;
    letter-spacing: 0.5px;
  }
  .holder {
    position: absolute;
    left: 45px;
    top: 196px;
  }
  .holder-name {
    font-family: "Cinzel", serif;
    font-weight: 700;
    color: var(--teal);
    font-size: 19px;
    letter-spacing: 0.3px;
  }
  .holder-specialty {
    color: var(--teal);
    font-size: 15px;
    margin-top: 2px;
  }
  .contact {
    list-style: none;
    margin-top: 34px;
  }
  .contact li {
    display: flex;
    align-items: center;
    gap: 10px;
    color: var(--ink);
    font-size: 15px;
    height: 21px;
  }
  .contact svg { width: 13px; height: 13px; fill: var(--ink); flex: none; }
</style>
</head>
<body>
  <header class="brand-mark">
    <div class="brand-name">Lucía Barrenechea</div>
  </header>

  <section class="card card--front">
    <div class="brand-name">Lucía Barrenechea</div>
  </section>

  <section class="card card--back">
    <div class="brand-name">Lucía Barrenechea</div>
    <div class="holder">
      <p class="holder-name">LUCÍA BARRENECHEA RUIZ</p>
      <p class="holder-specialty">Medicina Interna</p>
      <ul class="contact">
        <li>
          <svg viewBox="0 0 24 24" aria-hidden="true"><path d="M6.6 10.8c1.4 2.8 3.8 5.1 6.6 6.6l2.2-2.2c.3-.3.7-.4 1-.2 1.1.4 2.3.6 3.6.6.6 0 1 .4 1 1V20c0 .6-.4 1-1 1C10.6 21 3 13.4 3 4c0-.6.4-1 1-1h3.5c.6 0 1 .4 1 1 0 1.3.2 2.5.6 3.6.1.3 0 .7-.2 1z"/></svg>
          <span>5583617204</span>
        </li>
        <li>
          <svg viewBox="0 0 24 24" aria-hidden="true"><path d="M2 5h20v14H2z M2 5l10 8 10-8" fill="none"/><path d="M2 6.5V19h20V6.5l-10 7.5z"/><path d="M2 5h20l-10 7.5z"/></svg>
          <span>luciabarrenechearuiz@correovela.mx</span>
        </li>
      </ul>
    </div>
  </section>
</body>
</html>
```